Dental Business Card Design w/logo

Classic, elegant w/a touch of contemporary
Upscale dental facility located in Modesto CA
Specializing in restorative & general dentistry
Providing exceptional customer service to the community
Updates

I prefer script and not bold writing
If you can use the phone; fax and email icons instead of spelling them out, it would be great
No bold colors
Classy and elegant
In the back of the card I would like to see something like this
Your Next Appointment:
Mon     Tue    Wed    Thur (a box next to each of them for marking)
Date:_______________ at_____________ AM    PM  (a box next to them for marking)

Thank you

Target Market(s)

Well established professional

Industry/Entity Type

Dental

Contact Information for Business Card

Lavinteya Morbundi DMD
4176 Larkspur Rd
Suite F7
Modesto, CA 95355

Office: 209-731-5902
Fax: 209-731-8417
Email: morbundidmd@velmoranet.com

Requirements
Must have
• Unique classic logo
An easily repeatable design that can be used on letterhead and envelopes
Nice to have
• My initials incorporated into unique design
Should not have
• No cartoons or cheesy themes. This is a practice for the well established and professional individual.

```html
<!DOCTYPE html>
<html lang="en">
<head>
<meta charset="utf-8">
<title>Appointment Card – Lavinteya Morbundi DMD</title>
<link rel="stylesheet" href="https://fonts.googleapis.com/css2?family=Jost:wght@400&display=swap">
<style>
  :root {
    --page-bg: #ffffff;
    --card-bg: #ffffff;
    --card-border: #6f6f6f;
    --ink: #111111;
    --mark-tint: #c5e0e3;
  }
  html, body {
    margin: 0;
    padding: 0;
    width: 1200px;
    height: 900px;
    overflow: hidden;
    background: var(--page-bg);
  }
  .canvas {
    position: relative;
    width: 1200px;
    height: 900px;
    font-family: "Jost", "Futura", sans-serif;
    color: var(--ink);
  }
  .card {
    position: absolute;
    left: 371px;
    top: 61px;
    width: 467px;
    height: 792px;
    background: var(--card-bg);
    border: 1px solid var(--card-border);
    box-sizing: border-box;
  }
  .brand {
    position: absolute;
    left: 0;
    right: 0;
    top: 30px;
    height: 400px;
    display: flex;
    flex-direction: column;
    align-items: center;
    justify-content: center;
  }
  .brand-dot {
    width: 170px;
    height: 170px;
    border-radius: 50%;
    background: var(--mark-tint);
    margin-bottom: 34px;
  }
  .brand-name {
    margin: 0;
    text-align: center;
    font-size: 46px;
    font-weight: 400;
    line-height: 1.1;
    color: var(--mark-tint);
  }
  .appointment-title {
    position: absolute;
    left: 0;
    right: 0;
    top: 452px;
    margin: 0;
    text-align: center;
    font-size: 32px;
    font-weight: 400;
    letter-spacing: -0.4px;
    line-height: 1;
  }
  .day-list {
    position: absolute;
    left: 151px;
    top: 498px;
    margin: 0;
    padding: 0;
    list-style: none;
  }
  .day-list li {
    display: flex;
    align-items: center;
    height: 39.5px;
    font-size: 27px;
    line-height: 1;
  }
  .checkbox {
    display: inline-block;
    width: 13px;
    height: 13px;
    border: 2px solid var(--ink);
    margin-right: 11px;
    flex: none;
  }
  .field-row {
    position: absolute;
    display: flex;
    align-items: flex-end;
    font-size: 27px;
    line-height: 1;
  }
  .field-row.date { left: 66px; top: 696px; }
  .field-row.time { left: 44px; top: 734px; }
  .blank {
    display: inline-block;
    border-bottom: 2px solid var(--ink);
    margin-bottom: 2px;
  }
  .date .blank { width: 279px; margin-left: 1px; }
  .time .blank { width: 201px; margin-left: 1px; }
  .meridiem {
    display: inline-flex;
    align-items: center;
    margin-left: 8px;
  }
  .meridiem + .meridiem { margin-left: 24px; }
  .meridiem .checkbox { margin: 0 0 0 6px; }
</style>
</head>
<body>
  <main class="canvas">
    <section class="card" aria-label="Appointment reminder card">
      <div class="brand">
        <span class="brand-dot" aria-hidden="true"></span>
        <p class="brand-name">Lavinteya<br>Morbundi DMD</p>
      </div>
      <h1 class="appointment-title">Your Next Appointment:</h1>
      <ul class="day-list">
        <li><span class="checkbox"></span>Monday</li>
        <li><span class="checkbox"></span>Tuesday</li>
        <li><span class="checkbox"></span>Wednesday</li>
        <li><span class="checkbox"></span>Thursday</li>
      </ul>
      <div class="field-row date">Date:<span class="blank"></span></div>
      <div class="field-row time">
        at<span class="blank"></span>
        <span class="meridiem">AM<span class="checkbox"></span></span>
        <span class="meridiem">PM<span class="checkbox"></span></span>
      </div>
    </section>
  </main>
</body>
</html>
```